Company letter head and business card for new Indian Pharmaceutical Export company.

We need a letterhead and business card design for an Indian Pharmaceutical Export company.

The letter head needs to contain the following information.
Verona Healthline Pvt. Ltd.
Office No 4837 Plot No 52, Kestrel Heights, RT Lane, 400517, Maharashtra, India.
Email: info@verona-healthline.example
Phone: +91-8213460592
CIN: U58213MH2025PTC719264
GSTIN: (This number is still pending, we will add later)

The business card needs to contain:
Address:
Verona Healthline Pvt. Ltd.
Office No 4837 Plot No52, Kestrel Heights, RT Lane, 400517, MH, India.
Email: tobias@verona-healthline.example
Phone: +49-17638421956
Name on card: Tobias Wendlinger
Position: Director

The design for the letter head and business card should be simple but trustworthy.
Please use only Green and blue, same as in the attached logo.

```html
<!DOCTYPE html>
<html lang="en">
<head>
<meta charset="utf-8">
<title>Verona Healthline – Business Card</title>
<link rel="stylesheet" href="https://fonts.googleapis.com/css2?family=Montserrat:wght@300;400;700;800&family=Fira+Sans:ital,wght@0,500;1,500&display=swap">
<style>
  :root {
    --brand-blue: #1565a9;
    --brand-blue-dark: #0f5597;
    --brand-green: #86c440;
    --ink: #222326;
    --muted: #4a4b4f;
    --paper: #ffffff;
    --stage: #2b2b2d;
  }
  * { box-sizing: border-box; margin: 0; padding: 0; }
  html, body { width: 1200px; height: 875px; overflow: hidden; }
  body { background: var(--stage); position: relative; font-family: "Montserrat", sans-serif; }

  .card {
    position: absolute;
    width: 540px;
    height: 310px;
    border-radius: 18px;
    overflow: hidden;
    box-shadow: 0 14px 30px rgba(0,0,0,.45);
  }

  /* Front */
  .card--front { left: 50px; top: 100px; background: var(--brand-blue); }
  .front-brand {
    position: absolute; left: 0; right: 0; top: 50%;
    transform: translateY(-50%);
    display: flex; align-items: center; justify-content: center; gap: 14px;
  }
  .brand-dot { width: 26px; height: 26px; border-radius: 50%; background: var(--paper); }
  .front-brand .brand-name { color: var(--paper); font-weight: 800; font-size: 30px; letter-spacing: .3px; }

  /* Back */
  .card--back { left: 610px; top: 460px; background: var(--paper); }
  .back-brand {
    position: absolute; left: 150px; top: 34px;
    display: flex; align-items: center; gap: 10px;
  }
  .back-brand .brand-dot { width: 18px; height: 18px; background: var(--brand-blue); }
  .back-brand .brand-name { color: var(--brand-blue); font-weight: 800; font-size: 19px; }

  .person { position: absolute; right: 270px; top: 112px; text-align: right; }
  .person-name { color: var(--brand-blue); font-weight: 800; font-size: 25px; white-space: nowrap; }
  .person-role { color: var(--muted); font-weight: 400; font-size: 15px; margin-top: 2px; }

  .divider { position: absolute; left: 288px; top: 92px; width: 1.5px; height: 84px; background: var(--brand-green); }

  .contacts { position: absolute; left: 302px; top: 92px; list-style: none; }
  .contacts li {
    display: flex; align-items: center; gap: 8px;
    font-weight: 300; font-size: 12.5px; color: var(--ink); height: 27px; white-space: nowrap;
  }
  .contacts svg { width: 12px; height: 12px; flex: none; }

  .company { position: absolute; left: 60px; top: 196px; font-family: "Fira Sans", sans-serif; }
  .company-name { color: var(--brand-blue); font-style: italic; font-weight: 500; font-size: 15px; padding-left: 210px; }
  .company-address { color: var(--ink); font-weight: 500; font-size: 14.5px; margin-top: 6px; white-space: nowrap; }

  .card-band { position: absolute; left: 0; bottom: 0; width: 540px; height: 40px; }
</style>
</head>
<body>

  <section class="card card--front" aria-label="Business card front">
    <div class="front-brand">
      <span class="brand-dot"></span>
      <span class="brand-name">Verona Healthline</span>
    </div>
  </section>

  <section class="card card--back" aria-label="Business card back">
    <div class="back-brand">
      <span class="brand-dot"></span>
      <span class="brand-name">Verona Healthline</span>
    </div>

    <div class="person">
      <div class="person-name">Tobias Wendlinger</div>
      <div class="person-role">Director</div>
    </div>

    <span class="divider"></span>

    <ul class="contacts">
      <li>
        <svg viewBox="0 0 24 24" fill="#86c440"><path d="M6.6 10.8a15.1 15.1 0 006.6 6.6l2.2-2.2a1 1 0 011-.25 11.4 11.4 0 003.6.57 1 1 0 011 1V20a1 1 0 01-1 1A17 17 0 013 4a1 1 0 011-1h3.5a1 1 0 011 1 11.4 11.4 0 00.57 3.6 1 1 0 01-.25 1z"/></svg>
        +49-17638421956
      </li>
      <li>
        <svg viewBox="0 0 24 24"><rect x="2" y="5" width="20" height="14" rx="1.5" fill="#86c440"/><path d="M3 6l9 7 9-7" fill="none" stroke="#fff" stroke-width="1.8"/></svg>
        tobias@verona-healthline.example
      </li>
      <li>
        <svg viewBox="0 0 24 24" fill="none" stroke="#86c440" stroke-width="2"><circle cx="12" cy="12" r="9.5"/><path d="M2.5 12h19M12 2.5c3 3 3 16 0 19M12 2.5c-3 3-3 16 0 19"/></svg>
        www.verona-healthline.example
      </li>
    </ul>

    <div class="company">
      <div class="company-name">Verona Healthline Pvt. Ltd.</div>
      <div class="company-address">Office No 4837 Plot No52, Kestrel Heights, RT Lane, 400517, MH, India</div>
    </div>

    <svg class="card-band" viewBox="0 0 540 40" preserveAspectRatio="none" aria-hidden="true">
      <polygon points="0,32 300,32 292,40 0,40" fill="var(--brand-blue)"/>
      <polygon points="312,12 540,12 540,40 298,40" fill="var(--brand-green)"/>
    </svg>
  </section>

</body>
</html>
```